Microlight Aircraft Website Project

Need a website designed, or at least a template made, that my web programmer can work with here. We are a new manufacturer of microlight aircraft & powered hang gliders. Our company name is Brisk Fern. We manufacture portable utility aircraft in the Light Sport category (formerly known as Ultralights or Microlights). Our particular design is a 2-seat powered hang glider and caters to those who want to go explore the backcountry. We are not necessarily aviation nuts, but more into the development of a flying utility vehicle for extreme exploration and expeditions. We have been importing these aircraft from 3 countries for 15 years and have supplied over 200 expedition-quality aircraft world-wide. We are now manufacturing here in the US.

Industry/Entity Type

Manufacturer

Coding

Coded - Design and coding required

```html
<!DOCTYPE html>
<html lang="en">
<head>
<meta charset="utf-8">
<title>Brisk Fern — Contact</title>
<link rel="stylesheet" href="https://fonts.googleapis.com/css2?family=Chakra+Petch:wght@400;500&display=swap">
<style>
  :root {
    --sky-top: #98a3b3;
    --sky-mid: #7b8798;
    --ridge: #4a5566;
    --valley: #2c3440;
    --jacket: #9a3426;
    --text: #ffffff;
    --line: rgba(255, 255, 255, 0.85);
    --field-filled: rgba(255, 255, 255, 0.72);
    --field-text: #4a4f57;
    --button-fill: rgba(238, 176, 178, 0.75);
    --button-text: #4d4b4f;
  }
  * { box-sizing: border-box; margin: 0; padding: 0; }
  html, body {
    width: 1200px;
    height: 1000px;
    overflow: hidden;
  }
  body {
    position: relative;
    font-family: "Chakra Petch", sans-serif;
    color: var(--text);
  }
  .hero-backdrop {
    position: absolute;
    inset: 0;
    background:
      radial-gradient(ellipse 520px 200px at 380px 930px, var(--jacket) 0%, rgba(154, 52, 38, 0) 100%),
      linear-gradient(180deg, var(--sky-top) 0%, var(--sky-mid) 38%, var(--ridge) 58%, var(--valley) 100%);
  }
  .site-header {
    position: absolute;
    top: 0;
    left: 0;
    width: 1200px;
  }
  .brand {
    position: absolute;
    top: 86px;
    left: 0;
    width: 1200px;
    text-align: center;
    font-size: 17px;
    font-weight: 500;
    letter-spacing: 2px;
  }
  .main-nav {
    position: absolute;
    top: 170px;
    left: 190px;
    width: 818px;
    height: 42px;
    border-bottom: 1px solid var(--line);
  }
  .nav-item {
    position: absolute;
    top: 0;
    height: 41px;
    padding-top: 11px;
    font-size: 14px;
    letter-spacing: 3.2px;
    text-align: center;
    color: var(--text);
    text-decoration: none;
  }
  .nav-home { left: 70px; width: 120px; }
  .nav-about { left: 230px; width: 135px; }
  .nav-aircraft { left: 420px; width: 145px; }
  .nav-contact { left: 607px; width: 143px; border-top: 1px solid var(--line); }

  .contact-form {
    position: absolute;
    top: 286px;
    left: 273px;
    width: 652px;
  }
  .form-title {
    text-align: center;
    font-size: 26px;
    font-weight: 400;
    height: 40px;
    margin-bottom: 37px;
  }
  .field-label {
    display: block;
    text-align: center;
    font-size: 16px;
    line-height: 16px;
    height: 18px;
  }
  .field-input {
    display: block;
    width: 652px;
    height: 46px;
    margin-bottom: 32px;
    border: 1px solid var(--line);
    background: transparent;
    font-family: "Chakra Petch", sans-serif;
    font-size: 17px;
    color: var(--field-text);
    padding: 0 11px;
  }
  .field-input.is-filled { background: var(--field-filled); }
  .field-message {
    height: 157px;
    margin-bottom: 23px;
    resize: none;
  }
  .send-button {
    display: block;
    margin: 0 auto;
    width: 91px;
    height: 45px;
    border: 1px solid var(--line);
    background: var(--button-fill);
    color: var(--button-text);
    font-family: "Chakra Petch", sans-serif;
    font-size: 17px;
  }
  .section-title {
    position: absolute;
    top: 962px;
    left: 0;
    width: 1200px;
    text-align: center;
    font-size: 26px;
    font-weight: 400;
  }
</style>
</head>
<body>
  <div class="hero-backdrop" role="img" aria-label="View from a microlight cockpit over snow-capped mountains and a cloudy sky, pilot in a red jacket in the foreground"></div>

  <header class="site-header">
    <div class="brand">BRISK FERN</div>
    <nav class="main-nav">
      <a class="nav-item nav-home" href="#">HOME</a>
      <a class="nav-item nav-about" href="#">ABOUT US</a>
      <a class="nav-item nav-aircraft" href="#">AIRCRAFTS</a>
      <a class="nav-item nav-contact" href="#">CONTACT</a>
    </nav>
  </header>

  <form class="contact-form">
    <h1 class="form-title">Send us an e-mail</h1>
    <label class="field-label" for="full-name">Full Name</label>
    <input class="field-input is-filled" id="full-name" type="text" value="Mara Quinlan">
    <label class="field-label" for="email">E-mail Address</label>
    <input class="field-input" id="email" type="email">
    <label class="field-label" for="subject">Subject</label>
    <input class="field-input" id="subject" type="text">
    <label class="field-label" for="message">Message</label>
    <textarea class="field-input field-message" id="message"></textarea>
    <button class="send-button" type="button">Send</button>
  </form>

  <h2 class="section-title">Our location</h2>
</body>
</html>
```